Keystone Prime Water Tank

I primarily market the water tanks so want a business care that reflects that. I have attached the water tank logo. You have been working on our water tank so maybe we can use that on the card et. I am leaving as one sided but can be double sided if that works. The information that needs to be on the cards is as follows: Gerald T. Munro Phone numbers: Office 555-284-9137 Direct 555-619-2405 Mobile 555-372-5841 email address: gerald@fieldgearworks.com Address P.O. Box 8273 Larkmoor, OH 30512 Web Page: www.fieldgearworks.com. A lot to fit on the card. Thanks

```html
<!DOCTYPE html>
<html lang="en">
<head>
<meta charset="utf-8">
<title>Keystone Prime Water Tank – Business Card</title>
<link rel="stylesheet" href="https://fonts.googleapis.com/css2?family=Arimo:wght@400;700&display=swap">
<style>
  :root {
    --backdrop: #141414;
    --card: #2a2a2b;
    --card-edge: #e10000;
    --accent: #ee0000;
    --text: #f2f2f2;
    --divider: #bdbdbd;
  }
  * { margin: 0; padding: 0; box-sizing: border-box; }
  html, body {
    width: 1200px; height: 963px; overflow: hidden;
    background: var(--backdrop);
    font-family: "Arimo", Arial, sans-serif;
  }
  .stage {
    width: 1200px; height: 963px;
    display: flex; align-items: center; justify-content: center;
  }
  .business-card {
    width: 860px; height: 492px;
    background: var(--card);
    border-radius: 30px;
    box-shadow: 0 6px 0 var(--card-edge), 0 22px 40px rgba(0,0,0,.6);
    display: flex; align-items: center;
    padding: 0 56px 0 60px;
  }
  .brand {
    width: 360px;
    display: flex; align-items: center; gap: 16px;
  }
  .brand-mark {
    width: 34px; height: 34px; flex: none;
    background: var(--accent);
  }
  .brand-name {
    color: var(--text);
    font-weight: 700;
    font-size: 34px;
    line-height: 1.1;
    text-transform: uppercase;
  }
  .divider {
    width: 2px; height: 270px;
    background: var(--divider);
    margin: 0 44px 0 30px;
    flex: none;
  }
  .contact { color: var(--text); }
  .contact-name {
    color: var(--accent);
    font-size: 30px;
    font-weight: 400;
    margin-bottom: 14px;
  }
  .contact-address {
    font-size: 19px;
    line-height: 1.4;
    margin-bottom: 16px;
  }
  .contact-list { list-style: none; }
  .contact-list li {
    display: flex; align-items: center; gap: 12px;
    font-size: 19px;
    line-height: 1.55;
  }
  .contact-icon {
    width: 18px; height: 18px; flex: none;
    fill: none; stroke: var(--accent); stroke-width: 1.8;
    stroke-linecap: round; stroke-linejoin: round;
  }
  .contact-icon.solid { fill: var(--accent); stroke: none; }
</style>
</head>
<body>
<main class="stage">
  <article class="business-card">
    <div class="brand">
      <span class="brand-mark"></span>
      <span class="brand-name">Keystone Prime Water Tank</span>
    </div>
    <span class="divider"></span>
    <section class="contact">
      <h1 class="contact-name">Gerald T. Munro</h1>
      <p class="contact-address">P.O. Box 8273<br>Larkmoor, OH 30512</p>
      <ul class="contact-list">
        <li>
          <svg class="contact-icon solid" viewBox="0 0 24 24" aria-hidden="true"><path d="M6.6 10.8a15.5 15.5 0 0 0 6.6 6.6l2.2-2.2a1 1 0 0 1 1-.25 11.4 11.4 0 0 0 3.6.57 1 1 0 0 1 1 1V20a1 1 0 0 1-1 1A17 17 0 0 1 3 4a1 1 0 0 1 1-1h3.5a1 1 0 0 1 1 1c0 1.250.2 2.450.57 3.57a1 1 0 0 1-.25 1z"/></svg>
          555-284-9137
        </li>
        <li>
          <svg class="contact-icon" viewBox="0 0 24 24" aria-hidden="true"><rect x="6" y="2" width="12" height="20" rx="2"/><line x1="11" y1="18" x2="13" y2="18"/></svg>
          555-619-2405
        </li>
        <li>
          <svg class="contact-icon" viewBox="0 0 24 24" aria-hidden="true"><rect x="6" y="2" width="12" height="20" rx="2"/><line x1="11" y1="18" x2="13" y2="18"/></svg>
          555-372-5841
        </li>
        <li>
          <svg class="contact-icon" viewBox="0 0 24 24" aria-hidden="true"><rect x="2" y="5" width="20" height="14" rx="1"/><polyline points="2,5 12,13 22,5"/></svg>
          gerald@fieldgearworks.com
        </li>
        <li>
          <svg class="contact-icon" viewBox="0 0 24 24" aria-hidden="true"><circle cx="12" cy="12" r="10"/><line x1="2" y1="12" x2="22" y2="12"/><ellipse cx="12" cy="12" rx="4.5" ry="10"/></svg>
          www.fieldgearworks.com
        </li>
      </ul>
    </section>
  </article>
</main>
</body>
</html>
```